Tarvel Ridge LLC

Need Professional Business cards for New Investment Fund

Target Market(s)

High Quality investors

Industry/Entity Type

Financial

Contact Information for Business Card

Phone Number +1 555 284 6193
Name Pavel Orlinsky
Title Fund Manager
email po@FundTarvel.example
Website www.FundTarvel.example

Colors

Designer to choose colors to be used in the design.

Requirements
Must have
• Must have our Logo and all of the above. Must be made so lettering and loge can be raised

```html
<!DOCTYPE html>
<html lang="en">
<head>
<meta charset="utf-8">
<title>Tarvel Ridge LLC — Business Card</title>
<link href="https://fonts.googleapis.com/css2?family=Teko:wght@500&family=Raleway:wght@400;600&display=swap" rel="stylesheet">
<style>
  :root {
    --backdrop: #1f1f20;
    --front-bg: #435043;
    --back-bg: #121418;
    --accent: #4cbb47;
    --ink: #ffffff;
    --ink-soft: #e6e6e6;
  }
  html, body {
    margin: 0;
    padding: 0;
    width: 1200px;
    height: 900px;
    overflow: hidden;
    background: var(--backdrop);
  }
  .canvas {
    position: relative;
    width: 1200px;
    height: 900px;
  }
  .card {
    position: absolute;
    left: 285px;
    width: 630px;
    height: 360px;
    box-sizing: border-box;
  }
  .card--front {
    top: 70px;
    background: var(--front-bg);
  }
  .card--back {
    top: 470px;
    background: var(--back-bg);
  }
  .brand {
    position: absolute;
    left: 0;
    right: 0;
    top: 150px;
    display: flex;
    justify-content: center;
    align-items: center;
    gap: 14px;
  }
  .brand__square {
    width: 18px;
    height: 18px;
    background: var(--ink);
  }
  .brand__name {
    font-family: "Raleway", sans-serif;
    font-weight: 600;
    font-size: 34px;
    letter-spacing: 3px;
    color: var(--ink);
    text-transform: uppercase;
  }
  .front-bar {
    position: absolute;
    bottom: 0;
    left: 185px;
    width: 260px;
    height: 10px;
    background: var(--accent);
  }
  .accent {
    position: absolute;
    width: 5px;
    background: var(--accent);
  }
  .accent--left { left: 14px; top: 112px; height: 68px; }
  .accent--right { right: 14px; top: 200px; height: 78px; }
  .identity {
    position: absolute;
    right: 328px;
    top: 138px;
    text-align: right;
  }
  .identity__name {
    font-family: "Teko", sans-serif;
    font-weight: 500;
    font-size: 36px;
    line-height: 1;
    color: var(--ink);
    text-transform: uppercase;
  }
  .identity__title {
    font-family: "Raleway", sans-serif;
    font-weight: 400;
    font-size: 17px;
    color: var(--ink-soft);
    margin-top: 2px;
  }
  .divider {
    position: absolute;
    left: 314px;
    top: 136px;
    width: 1px;
    height: 72px;
    background: var(--accent);
  }
  .contacts {
    position: absolute;
    left: 332px;
    top: 136px;
    margin: 0;
    padding: 0;
    list-style: none;
  }
  .contacts li {
    display: flex;
    align-items: center;
    gap: 10px;
    height: 25px;
    font-family: "Raleway", sans-serif;
    font-size: 17px;
    color: var(--ink);
  }
  .contacts svg {
    width: 15px;
    height: 15px;
    flex: none;
  }
</style>
</head>
<body>
<main class="canvas">
  <section class="card card--front" aria-label="Card front">
    <div class="brand">
      <span class="brand__square"></span>
      <span class="brand__name">Tarvel Ridge</span>
    </div>
    <div class="front-bar"></div>
  </section>

  <section class="card card--back" aria-label="Card back">
    <div class="accent accent--left"></div>
    <div class="accent accent--right"></div>

    <div class="identity">
      <div class="identity__name">Pavel Orlinsky</div>
      <div class="identity__title">Title Fund Manager</div>
    </div>

    <div class="divider"></div>

    <ul class="contacts">
      <li>
        <svg viewBox="0 0 16 16" aria-hidden="true"><path d="M4 1.5l2.2 3-1.3 1.6a9 9 0 0 0 5 5l1.6-1.3 3 2.2-1.3 2.5C8 14.5 1.5 8 1.5 2.8z" fill="var(--accent)"/></svg>
        +1 555 284 6193
      </li>
      <li>
        <svg viewBox="0 0 16 16" aria-hidden="true"><rect x="1.5" y="3.5" width="13" height="9" fill="none" stroke="var(--accent)" stroke-width="1.4"/><path d="M1.5 3.5L8 9l6.5-5.5" fill="none" stroke="var(--accent)" stroke-width="1.4"/></svg>
        po@FundTarvel.example
      </li>
      <li>
        <svg viewBox="0 0 16 16" aria-hidden="true"><g fill="none" stroke="var(--accent)" stroke-width="1.2"><circle cx="8" cy="8" r="6.5"/><ellipse cx="8" cy="8" rx="3" ry="6.5"/><path d="M1.5 8h13M2.5 4.8h11M2.5 11.2h11"/></g></svg>
        www.FundTarvel.example
      </li>
    </ul>
  </section>
</main>
</body>
</html>
```